Medical Mgmt Outsourcing in Need of Eye Catching Brochure

We need a brochure with an eye catching design. We're looking for an 8x8 trifold brochure. We are a claims management and outsourcing company located in the Detroit area. We are currently under going some changes and revamping ourselves. We would like the colors blue, yellow, white and grey as a definite. I've included our company logo in the uploads, our services, and two pictures of our server room that we would like to use for our technical services page. We have three types of services - administrative, professional, technical. We are also looking for a design with a swirl in it. I have also uploaded a picture of the type of swirl graphics we are looking for.

Industry/Entity Type

It Company

Colors
0355a3
3276b5
85abd2
fbed22
fbee3e
aaaaaa
959595
5c5c5c

Requirements
Must have
• Colors: Blue, grey, white, yellow
• Design: Swirl
• Looking for more of a professional approach to the brochure.
• Services must be in the order 1. Administrative 2. Professional 3. Technical
• We are looking for just bullet points of services with no description of what they are.
Should not have
• The words "outsourcing" and "BPO"

```html
<!DOCTYPE html>
<html lang="en">
<head>
<meta charset="utf-8">
<title>Corvane Associates – Services Brochure</title>
<link rel="stylesheet" href="https://fonts.googleapis.com/css2?family=Oswald:wght@500;600&family=Arimo:wght@400;700&display=swap">
<style>
  :root {
    --stage: #ecebe8;
    --paper: #f4f4f5;
    --teal: #10a699;
    --teal-deep: #0a7f8a;
    --blue-deep: #0c5d92;
    --gold: #e4b320;
    --gold-light: #f6d75a;
    --ink: #4f4f4f;
    --ink-dark: #222;
    --box-grey: #d3d3d5;
    --box-tint: #e2ebe8;
    --white: #ffffff;
  }
  * { box-sizing: border-box; margin: 0; padding: 0; }
  html, body { width: 1200px; height: 654px; overflow: hidden; }
  body { background: var(--stage); font-family: "Arimo", Arial, sans-serif; color: var(--ink); position: relative; }

  .page { position: absolute; top: 42px; width: 570px; height: 568px; background: var(--paper); overflow: hidden; box-shadow: 0 2px 8px rgba(0,0,0,.18); }
  .page--front { left: 19px; }
  .page--inside { left: 613px; }

  .header { position: absolute; left: 0; top: 0; width: 570px; height: 140px; }
  .header svg { position: absolute; inset: 0; }
  .tagline { position: absolute; font-family: "Oswald", sans-serif; font-weight: 500; font-size: 21px; color: var(--white); letter-spacing: .2px; }
  .tagline--left { left: 39px; top: 44px; }
  .tagline--right { left: 407px; top: 38px; }
  .brand { position: absolute; left: 210px; top: 16px; width: 150px; text-align: center; font-family: "Oswald", sans-serif; font-weight: 600; color: var(--white); line-height: 1; }
  .brand-name { display: block; font-size: 36px; letter-spacing: 1px; }
  .brand-sub { display: block; font-size: 13px; letter-spacing: 3.2px; margin-top: 6px; }

  .footer { position: absolute; left: 0; bottom: 0; width: 570px; height: 42px; }
  .footer svg { position: absolute; inset: 0; }

  .text { position: absolute; font-size: 9.6px; line-height: 1.27; }
  .intro { left: 47px; top: 157px; width: 480px; font-size: 10px; }
  .intro strong { color: var(--ink-dark); }

  .section-icon { position: absolute; width: 22px; height: 24px; border-radius: 11px 11px 4px 4px; background: #3a3a3a; }
  .section-title { position: absolute; height: 24px; padding-left: 6px; display: flex; align-items: center; background: linear-gradient(90deg, var(--teal-deep), var(--teal) 80%, #7fd2b8); border-bottom: 2px solid var(--gold); font-family: "Oswald", sans-serif; font-weight: 500; font-style: italic; font-size: 18px; color: var(--white); letter-spacing: .6px; }

  .service-box { position: absolute; left: 314px; width: 219px; background: var(--box-grey); font-size: 9.5px; line-height: 1.42; padding: 3px 8px; }
  .service-box li { list-style: none; position: relative; padding-left: 9px; }
  .service-box li::before, .bullets li::before { content: ""; position: absolute; left: 0; top: 3.5px; width: 5px; height: 5px; background: var(--teal); }
  .service-box .i1 { margin-left: 28px; } .service-box .i2 { margin-left: 34px; } .service-box .i3 { margin-left: 86px; } .service-box .i4 { margin-left: 22px; }

  .cost-title { position: absolute; left: 47px; top: 459px; font-weight: 700; font-size: 10.4px; color: var(--teal); }
  .bullets { position: absolute; left: 48px; top: 474px; font-size: 9.6px; line-height: 1.27; }
  .bullets li { list-style: none; position: relative; padding-left: 9px; }

  .tech-visual { position: absolute; left: 315px; top: 458px; width: 218px; height: 74px; background: radial-gradient(circle at 30% 55%, #e9f1ff 0, #6b86d6 14%, #20308a 45%, #070b35 100%); }

  .detail { position: absolute; width: 227px; font-size: 9.2px; line-height: 1.24; padding: 2px 4px 4px 6px; }
  .detail--tint { background: var(--box-tint); }
  .detail h3 { font-size: 10.4px; font-weight: 700; color: var(--teal); position: relative; padding-left: 8px; margin-left: -8px; margin-bottom: 1px; }
  .detail h3::before { content: ""; position: absolute; left: 0; top: 3px; border-left: 5px solid var(--teal); border-top: 3px solid transparent; border-bottom: 3px solid transparent; }
  .detail u { text-decoration-color: var(--teal); }
</style>
</head>
<body>

<section class="page page--front">
  <header class="header">
    <svg viewBox="0 0 570 140" width="570" height="140" aria-hidden="true">
      <defs>
        <linearGradient id="band1" x1="0" y1="0" x2="1" y2="1">
          <stop offset="0" stop-color="#0c5d92"/><stop offset=".45" stop-color="#10a699"/><stop offset="1" stop-color="#0b6f95"/>
        </linearGradient>
        <linearGradient id="gold1" x1="0" x2="1"><stop offset="0" stop-color="#e4b320"/><stop offset=".5" stop-color="#f6d75a"/><stop offset="1" stop-color="#d59a14"/></linearGradient>
      </defs>
      <path d="M0 0H570V98C520 110 470 130 390 132C300 134 220 108 130 104C70 102 30 110 0 118Z" fill="url(#gold1)"/>
      <path d="M0 0H570V90C520 102 470 122 390 124C300 126 220 100 130 96C70 94 30 102 0 110Z" fill="url(#band1)"/>
    </svg>
    <span class="tagline tagline--left">Your Potential!</span>
    <div class="brand"><span class="brand-name">CORVANE</span><span class="brand-sub">ASSOCIATES</span></div>
    <span class="tagline tagline--right">Is Our Passion!</span>
  </header>

  <p class="text intro">As an Information, Technology, and Business Service Provider, <strong>Corvane offers</strong> a comprehensive line of administrative, professional, and technical services. Experience the advantages of higher profitability by utilizing our solutions.</p>

  <div class="section-icon" role="img" aria-label="Support agent icon" style="left:37px;top:199px"></div>
  <h2 class="section-title" style="left:61px;top:204px;width:196px">Administrative Services</h2>
  <p class="text" style="left:47px;top:235px;width:245px">Our experienced teams are trained to effectively perform a variety of back-office services to support the claim payment process.</p>

  <div class="section-icon" role="img" aria-label="Support agent icon" style="left:37px;top:283px"></div>
  <h2 class="section-title" style="left:61px;top:288px;width:196px">Professional Services</h2>
  <p class="text" style="left:47px;top:319px;width:250px">Subject Matter Experts comprise every aspect of our professional services to improve business workflow, business workflow consulting, and claim automation solutions.</p>

  <div class="section-icon" role="img" aria-label="Support agent icon" style="left:37px;top:377px"></div>
  <h2 class="section-title" style="left:61px;top:382px;width:196px">Technical Services</h2>
  <p class="text" style="left:47px;top:413px;width:250px">EDI Specialist, Developers and Claims Management Specialists are available to support any aspect of your system development.</p>

  <h3 class="cost-title">Cost Containment Products &amp; Services</h3>
  <ul class="bullets">
    <li>IVR Fax Call Center Solution</li>
    <li>Medical and Dental Network Re-Pricing</li>
    <li>Out-of-Network Provider Contracting</li>
    <li>Electronic Provider EOB ‘s and Payments</li>
  </ul>

  <ul class="service-box" style="top:192px;height:101px">
    <li class="i3">Online Data Entry</li>
    <li>Mailroom &amp; Scanning</li>
    <li class="i2">Paper &amp; EDI Claim Clearinghouse</li>
    <li>Member and Provider Maintenance</li>
    <li class="i4">Flex Processing Medical Enrollments</li>
    <li>Cobra Processing</li>
    <li class="i3">Provider Call Center</li>
  </ul>
  <ul class="service-box" style="top:304px;height:64px">
    <li>Plan Building</li>
    <li class="i1">Plan Auditing &amp; Testing</li>
    <li>Auto-Payment Improvement Examining</li>
    <li class="i1">Auditing</li>
  </ul>
  <ul class="service-box" style="top:382px;height:64px">
    <li>Claim Management</li>
    <li class="i1">System Consulting</li>
    <li>EDI Configuration Custom Programming and Software Development</li>
  </ul>

  <div class="tech-visual" role="img" aria-label="Glowing binary data tunnel image"></div>

  <footer class="footer">
    <svg viewBox="0 0 570 42" width="570" height="42" aria-hidden="true">
      <defs><linearGradient id="foot1" x1="0" x2="1"><stop offset="0" stop-color="#0c6d8f"/><stop offset=".5" stop-color="#10a699"/><stop offset="1" stop-color="#0c6d8f"/></linearGradient></defs>
      <path d="M0 26C150 8 350 0 570 20V42H0Z" fill="#e4b320"/>
      <path d="M0 31C150 13 350 5 570 25V42H0Z" fill="url(#foot1)"/>
    </svg>
  </footer>
</section>

<section class="page page--inside">
  <header class="header">
    <svg viewBox="0 0 570 140" width="570" height="140" aria-hidden="true">
      <defs>
        <linearGradient id="band2" x1="0" y1="0" x2="1" y2="1">
          <stop offset="0" stop-color="#0c5d92"/><stop offset=".45" stop-color="#10a699"/><stop offset="1" stop-color="#0b6f95"/>
        </linearGradient>
        <linearGradient id="gold2" x1="0" x2="1"><stop offset="0" stop-color="#e4b320"/><stop offset=".5" stop-color="#f6d75a"/><stop offset="1" stop-color="#d59a14"/></linearGradient>
      </defs>
      <path d="M0 0H570V98C520 110 470 130 390 132C300 134 220 108 130 104C70 102 30 110 0 118Z" fill="url(#gold2)"/>
      <path d="M0 0H570V90C520 102 470 122 390 124C300 126 220 100 130 96C70 94 30 102 0 110Z" fill="url(#band2)"/>
    </svg>
    <span class="tagline tagline--left">Your Potential!</span>
    <div class="brand"><span class="brand-name">CORVANE</span><span class="brand-sub">ASSOCIATES</span></div>
    <span class="tagline tagline--right">Is Our Passion!</span>
  </header>

  <div class="section-icon" role="img" aria-label="Support agent icon" style="left:37px;top:153px"></div>
  <h2 class="section-title" style="left:61px;top:158px;width:207px">Administrative Services</h2>
  <p class="text" style="left:47px;top:187px;width:485px;font-size:9.8px">Our experienced teams are trained to effectively perform a variety of back-office services to support the claim payment process.</p>

  <div class="detail" style="left:42px;top:218px">
    <h3>Online Data Entry</h3>
    Reduces backlogs quickly with minimal setup Corvane Operators can index claims, EOB’s, and Re-pricing data directly into your adjudication software system.
  </div>
  <div class="detail detail--tint" style="left:42px;top:288px;height:69px">
    <h3>Flex Processing and Medical Enrollments</h3>
    Stabilize the workflow during seasonal peaks.Managing your seasonal Enrollment or Flexprocessing fluctuations are simple and under control by implementing our solutions.
  </div>
  <div class="detail" style="left:42px;top:363px">
    <h3>Mail Room &amp; Scanning</h3>
    Providers can now submit paper claims to a Corvane P.O. Box . All claims will be scanned into an electronic format and either hosted on a secured
  </div>
  <div class="detail detail--tint" style="left:42px;top:437px;height:78px">
    <h3>Paper &amp; EDI Claim Clearinghouse</h3>
    Claim images will be converted to electronic format and combined with claims received through our clearinghouse partners. All claims will be will be formatted for easy entry directly into your adjudication system.
  </div>

  <div class="detail detail--tint" style="left:306px;top:216px;height:99px">
    <h3>Provider Call Center</h3>
    Transitioning your provider calls to Corvane allows your CSR’s to focus on member calls. Our objective is to <u>reduce call center CSR compliment</u> by implementing technology solutions to handle most Provider inquiries -Claim Status, Eligibility, Authorizations, and more…
  </div>
  <div class="detail" style="left:306px;top:322px">
    <h3>Claim Examining</h3>
    Reduce HR requirements and pay claims quicker. Our experienced examiners can quickly begin processing claims, perform maintenance tasks and more… to meet or <u>exceed your service level requirements and reduce backlog</u> conditions by taking advantage of 24 hour resources.
  </div>
  <div class="detail detail--tint" style="left:306px;top:425px;height:86px">
    <h3>Provider and Member Maintenance</h3>
    Improve auto adjudication rates. Updates are managed daily to keep your provider and member data current and accurate. For example; updating NPI codes can support HIPAA compliance, or provider cleanup services to identify and flag duplicate records.
  </div>

  <footer class="footer">
    <svg viewBox="0 0 570 42" width="570" height="42" aria-hidden="true">
      <defs><linearGradient id="foot2" x1="0" x2="1"><stop offset="0" stop-color="#0c6d8f"/><stop offset=".5" stop-color="#10a699"/><stop offset="1" stop-color="#0c6d8f"/></linearGradient></defs>
      <path d="M0 26C150 8 350 0 570 20V42H0Z" fill="#e4b320"/>
      <path d="M0 31C150 13 350 5 570 25V42H0Z" fill="url(#foot2)"/>
    </svg>
  </footer>
</section>

</body>
</html>
```